We Fitness company called 'Jump2Joy Fitness' and we intends to encourage and promote a healthier lifestyle for the local communities by offering services such as fitness classes, boot camps, one to one personal training to name a few, all to fulfil our great vision of a healthier and fitter community. Now we are just about to open a new Bootcamp Classes for Erith community.

Target Market(s)

Men and women, all race, age 15 and over

Industry/Entity Type

Fitness

Colors
3176b5
f37122
0c5ba6
f78f20
abd037
ffc214

Requirements
Must have
• group work out pictures and writing in Blue and orange colours and the company logo.
Nice to have
• I would like the designer to play around in arranging the informations

```html
<!DOCTYPE html>
<html lang="en">
<head>
<meta charset="utf-8">
<title>J2J Bootcamp – Jump2Joy Fitness</title>
<link href="https://fonts.googleapis.com/css2?family=Montserrat:wght@600;700;800;900&family=Open+Sans:wght@400;600;700&display=swap" rel="stylesheet">
<style>
  :root{
    --blue:#3176b5;
    --blue-dark:#0c5ba6;
    --orange:#f37122;
    --orange-light:#f78f20;
    --green:#abd037;
    --green-dark:#7fa81f;
    --yellow:#ffc214;
    --white:#ffffff;
    --ink:#1d3f66;
  }
  *{box-sizing:border-box;margin:0;padding:0}
  html,body{width:849px;height:1200px;overflow:hidden;background:#fff}
  body{font-family:"Open Sans",Arial,sans-serif}
  .flyer{position:relative;width:849px;height:1200px;overflow:hidden;background:var(--white)}

  .hero-photo{position:absolute;left:0;top:0;width:849px;height:735px;
    background:linear-gradient(180deg,#9ec7e8 0%,#c9dced 35%,#b7b39a 60%,#8c8f62 100%)}
  .hero-panel{position:absolute;left:0;top:0;width:849px;height:735px}

  .brand{position:absolute;left:40px;top:40px;display:flex;align-items:center;gap:12px}
  .brand-dot{width:58px;height:58px;border-radius:50%;background:var(--orange)}
  .brand-name{font-family:"Montserrat",sans-serif;font-weight:800;font-size:28px;color:var(--blue-dark);line-height:1}
  .brand-tag{position:absolute;left:40px;top:108px;font-size:11px;font-weight:700;color:var(--blue);letter-spacing:1px}

  .title{position:absolute;left:38px;top:190px;font-family:"Montserrat",sans-serif;font-weight:900;font-size:170px;line-height:1;color:var(--orange);letter-spacing:-4px}
  .subtitle{position:absolute;left:42px;top:362px;font-family:"Montserrat",sans-serif;font-weight:900;font-size:84px;line-height:1;color:var(--blue-dark);letter-spacing:-1px}
  .strap{position:absolute;left:44px;top:458px;font-family:"Montserrat",sans-serif;font-weight:700;font-size:22px;color:var(--blue-dark)}

  .limited{position:absolute;right:-58px;top:42px;width:260px;padding:8px 0;transform:rotate(45deg);background:var(--orange);text-align:center;color:var(--white);font-family:"Montserrat",sans-serif;font-weight:800;line-height:1.05}
  .limited .big{font-size:22px;display:block}
  .limited .small{font-size:14px;display:block}

  .price{position:absolute;left:40px;top:515px;width:310px;height:120px}
  .price-text{position:absolute;left:58px;top:537px;color:var(--white);font-family:"Montserrat",sans-serif;font-weight:900;line-height:1}
  .price-text .from-label{font-size:28px;display:block}
  .price-text .from-value{font-size:52px;display:block;margin-top:6px}

  .weeks{position:absolute;left:445px;top:533px;width:404px;height:80px;background:var(--white);padding:12px 0 0 30px}
  .weeks h2{font-family:"Montserrat",sans-serif;font-weight:800;font-size:21px;color:var(--orange);white-space:nowrap}
  .weeks p{font-size:16px;font-weight:600;color:var(--blue-dark);margin-top:4px}

  .now{position:absolute;left:420px;top:615px;width:429px;height:110px;background:rgba(12,91,166,.92);padding:12px 0 0 24px;color:var(--white)}
  .now h2{font-family:"Montserrat",sans-serif;font-weight:800;font-size:21px;color:var(--orange-light);margin-bottom:6px}
  .now li{list-style:none;font-size:15px;line-height:1.4;white-space:nowrap}
  .now li::before{content:"• ";}

  .training{position:absolute;left:0;top:735px;width:849px;height:180px;background:linear-gradient(90deg,var(--green) 0%,#8fbf2c 45%,#56a26a 100%);display:flex;padding:20px 34px 0}
  .training h3{font-family:"Montserrat",sans-serif;font-weight:800;font-size:18px;color:var(--white);margin-bottom:8px;white-space:nowrap}
  .training li{list-style:none;font-size:16px;color:var(--white);line-height:1.4}
  .training li::before{content:"• ";}
  .build{width:340px}
  .focus{flex:1}
  .focus ul{display:grid;grid-template-columns:180px 180px}

  .challenge{position:absolute;left:0;top:915px;width:849px;height:135px;background:linear-gradient(180deg,var(--yellow),var(--orange-light));text-align:center;padding-top:12px}
  .challenge .lead{font-family:"Montserrat",sans-serif;font-weight:800;font-size:17px;line-height:1.25;color:var(--blue-dark)}
  .challenge .note{font-size:15px;color:var(--white);font-weight:600;margin-top:3px;line-height:1.3}
  .challenge .levels{font-family:"Montserrat",sans-serif;font-weight:800;font-size:17px;line-height:1.3;color:var(--blue-dark)}

  .details{position:absolute;left:0;top:1050px;width:849px;height:150px;background:linear-gradient(90deg,var(--blue-dark),var(--blue));color:var(--white);display:flex;padding:14px 34px 0}
  .schedule{width:500px;font-size:13px;line-height:1.55}
  .schedule .row{display:flex}
  .schedule dt{width:105px;font-weight:700;flex:none}
  .schedule dd{white-space:nowrap}
  .register{flex:1;border-left:2px solid rgba(255,255,255,.5);padding-left:20px;font-size:13.5px;line-height:1.4}
  .register .contact{display:flex;align-items:center;gap:8px;font-weight:700;margin-top:4px}
  .register svg{flex:none}
</style>
</head>
<body>
<main class="flyer">
  <div class="hero-photo" role="img" aria-label="Group of people doing an outdoor bootcamp workout with kettlebells on grass"></div>

  <svg class="hero-panel" viewBox="0 0 849 735" aria-hidden="true">
    <path d="M0 0 H560 C520 120 500 260 470 400 C455 460 440 500 420 520 H0 Z" fill="#ffffff"/>
  </svg>

  <div class="brand">
    <span class="brand-dot"></span>
    <span class="brand-name">Jump2Joy Fitness</span>
  </div>
  <div class="brand-tag">BE ACTIVE · BE POSITIVE · BE HAPPY</div>

  <div class="limited"><span class="big">LIMITED</span><span class="small">SPACES AVAILABLE</span></div>

  <h1 class="title">J2J</h1>
  <div class="subtitle">BOOTCAMP</div>
  <div class="strap">Family &amp; community healthy lifestyle</div>

  <svg class="price" viewBox="0 0 310 120" aria-hidden="true">
    <path d="M0 10 L300 0 L310 110 L10 120 Z" fill="#f37122"/>
    <path d="M0 10 L300 0 L304 10 L6 20 Z" fill="#f78f20"/>
  </svg>
  <div class="price-text"><span class="from-label">PRICES STARTING</span><span class="from-value">FROM £5</span></div>

  <section class="weeks">
    <h2>10 – 12 WEEKS BODY CHANGE</h2>
    <p>Get Fit, Stay Fit &amp; Feel Great</p>
  </section>

  <section class="now">
    <h2>NOW IS THE TIME TO:</h2>
    <ul>
      <li>Have the right shape you have been dreaming off</li>
      <li>Lose weight and Tone up</li>
    </ul>
  </section>

  <section class="training">
    <div class="build">
      <h3>BUILD &amp; INCREASE:</h3>
      <ul>
        <li>Strength and Endurance</li>
        <li>Cardio Fitness</li>
        <li>Improve your energy &amp; Vitality</li>
      </ul>
    </div>
    <div class="focus">
      <h3>OUR INTENSE TRAINING FOCUSES ON:</h3>
      <ul>
        <li>Strength</li><li>Squatting</li>
        <li>Cardio</li><li>Pulling</li>
        <li>Agility</li><li>Twisting</li>
        <li>Flexibility</li><li>Pressing</li>
      </ul>
    </div>
  </section>

  <section class="challenge">
    <p class="lead">COME AND CHALLENGE YOUR BODY THROUGH THE RIGHT<br>INTENSITY EXERCISE TRAINING WITH OUR PROFESSIONAL<br>PERSONAL TRAINERS AND DIET NUTRITIONIST.</p>
    <p class="note">Take part in the J2J Fitness challenge</p>
    <p class="levels">BEGGINNER OR EXPERIENCE. ALL LEVES ARE WELCOME</p>
  </section>

  <section class="details">
    <dl class="schedule">
      <div class="row"><dt>Location:</dt><dd>Marsh Lane Community Hall, Riverside Road, Erith DA8 9ZZ</dd></div>
      <div class="row"><dt>Days:</dt><dd>Monday, Tuesday &amp; Friday</dd></div>
      <div class="row"><dt>Time:</dt><dd>Morning (9.30am-10.30am) &amp; (10.30am-11.30am)</dd></div>
      <div class="row"><dt>Day &amp; Time:</dt><dd>Saturday 9am – 10am</dd></div>
      <div class="row"><dt>Days:</dt><dd>Thursday &amp; Friday</dd></div>
      <div class="row"><dt>Evening:</dt><dd>(6.15pm-7.15pm &amp; 7.30pm-8.30pm)</dd></div>
    </dl>
    <div class="register">
      <p>To Register and for more info visit our website, give us a call or email us on:</p>
      <p class="contact"><svg width="16" height="16" viewBox="0 0 16 16"><circle cx="8" cy="8" r="7" fill="none" stroke="#fff" stroke-width="1.5"/><path d="M1 8h14M8 1c3 3 3 11 0 14M8 1c-3 3-3 11 0 14" fill="none" stroke="#fff" stroke-width="1.2"/></svg>www.jump2joyfitness.co.uk</p>
      <p class="contact"><svg width="16" height="16" viewBox="0 0 16 16"><rect x="1" y="3" width="14" height="10" rx="1" fill="none" stroke="#fff" stroke-width="1.5"/><path d="M1 4l7 5 7-5" fill="none" stroke="#fff" stroke-width="1.5"/></svg>info@jump2joyfitness.co.uk</p>
      <p class="contact"><svg width="16" height="16" viewBox="0 0 16 16"><path d="M4 1l3 3-2 2c1 2 3 4 5 5l2-2 3 3-2 3C7 15 1 9 1 3z" fill="#fff"/></svg>02080001234</p>
    </div>
  </section>
</main>
</body>
</html>
```